Rehab/fitness Business card design

I need a design that promotes "A peak ridge base for movers". services include assessment, massage, physiotherapy, pilates, suspension training, kinesiotaping in any combination.
I would like to bring the design into my website, flyers etc

Target Market(s)

athletes from beginner to elite - any age, male and female

Industry/Entity Type

Shop

Contact Information for Business Card

Peak-Ridge-Base for Movers
17 Halden Rise, Marlow Heights, Kestrel Bay
027 418 7093
kerry.dunlow@vestmail.test

Logo Text

Logo styles of interest
Abstract Logo
Requirements
Nice to have
• Blue colour theme

```html
<!DOCTYPE html>
<html lang="en">
<head>
<meta charset="utf-8">
<title>Peak-Ridge-Base for Movers — Business Card</title>
<link href="https://fonts.googleapis.com/css2?family=Orbitron:wght@500&family=Arimo:wght@400&display=swap" rel="stylesheet">
<style>
  :root {
    --backdrop: #e9e7e4;
    --navy-deep: #1e1d5c;
    --navy-glow: #3b4593;
    --band-light: #ffffff;
    --band-edge: #e2e0e2;
    --ink: #2a2a78;
    --address-ink: #f2f2f8;
  }
  html, body {
    margin: 0;
    padding: 0;
    width: 1200px;
    height: 1181px;
    overflow: hidden;
    background: var(--backdrop);
  }
  .canvas {
    position: relative;
    width: 1200px;
    height: 1181px;
  }
  .card {
    position: absolute;
    left: 185px;
    width: 830px;
    height: 477px;
    border-radius: 32px;
    overflow: hidden;
    background: radial-gradient(ellipse 62% 75% at 50% 35%, var(--navy-glow) 0%, #2d3478 45%, var(--navy-deep) 100%);
    box-shadow: 0 10px 22px rgba(0,0,0,0.35);
  }
  .card--front { top: 78px; }
  .card--back { top: 617px; height: 476px; }
  .band {
    position: absolute;
    left: 0;
    width: 100%;
    height: 140px;
    background: radial-gradient(ellipse 55% 90% at 50% 45%, var(--band-light) 0%, #f4f3f4 45%, var(--band-edge) 100%);
    box-shadow: 0 3px 5px rgba(10,10,50,0.45);
    display: flex;
    align-items: center;
    justify-content: center;
  }
  .card--front .band { top: 169px; }
  .card--back .band { top: 167px; }
  .tagline {
    margin: 0;
    font-family: "Orbitron", sans-serif;
    font-weight: 500;
    font-size: 22px;
    letter-spacing: 9px;
    text-transform: uppercase;
    color: var(--ink);
    text-shadow: 1px 2px 3px rgba(0,0,40,0.35);
    transform: skewX(-8deg) translateY(6px);
  }
  .contact-row {
    list-style: none;
    margin: 0;
    padding: 0;
    display: flex;
    gap: 36px;
    font-family: "Arimo", sans-serif;
    font-size: 16px;
    letter-spacing: -0.6px;
    color: var(--ink);
    text-shadow: 1px 1px 2px rgba(0,0,40,0.3);
    transform: translateY(6px);
  }
  .contact-row li { display: flex; align-items: center; }
  .contact-row .bullet {
    display: inline-block;
    width: 8px;
    height: 8px;
    background: var(--ink);
    margin: 0 8px;
  }
  .address {
    position: absolute;
    left: 0;
    right: 0;
    top: 443px;
    margin: 0;
    text-align: center;
    font-family: "Arimo", sans-serif;
    font-size: 16px;
    letter-spacing: -0.5px;
    color: var(--address-ink);
  }
</style>
</head>
<body>
<main class="canvas">
  <section class="card card--front" aria-label="Card front">
    <div class="band">
      <h1 class="tagline">Peak-Ridge-Base for Movers</h1>
    </div>
  </section>

  <section class="card card--back" aria-label="Card back">
    <div class="band">
      <ul class="contact-row">
        <li>Phone<span class="bullet"></span>027 418 7093</li>
        <li>Web<span class="bullet"></span>www.peakridgebase.test</li>
        <li>Email<span class="bullet"></span>kerry.dunlow@vestmail.test</li>
      </ul>
    </div>
    <p class="address">17 Halden Rise, Marlow Heights, Kestrel Bay</p>
  </section>
</main>
</body>
</html>
```